Professional law firm looking for new professional and eye-catching business card design

Law firm in need of new business card design using existing firm logo and firm colors on thick card stock. Firm colors are navy blue, cyan blue, and gray. Please use firm's logo either on the back of the card or on the front and back. I am looking for something eye-catching and resonating but also professional.

Target Market(s)

Law firm growth by attracting clients with professional, creative, and attractive business cards.

Industry/Entity Type

Legal/Law Firm

Contact Information for Business Card

Name: Derek T. Halloway, Esq., Address: 517 E. Quintley Blvd., P.O. Box 641, Tavares, FL 32790, Phone numbers: (352) 555-0187 Office, (352) 555-0142 Fax, email address: DerekH@hqlegalfx.com, website: www.HQLegalFX.com

Font styles to use
Other font styles liked:
• Font as close as possible to matching law firm logo.

Requirements
Must have
• Must have business card details and law firm logo with law firm colors.

```html
<!DOCTYPE html>
<html lang="en">
<head>
<meta charset="utf-8">
<title>Halloway &amp; Quintley, P.A. – Business Card</title>
<link href="https://fonts.googleapis.com/css2?family=DM+Serif+Display&family=Montserrat:wght@400;500&display=swap" rel="stylesheet">
<style>
  :root {
    --backdrop: #2e241b;
    --navy: #13294a;
    --navy-deep: #0c1c34;
    --navy-mid: #1c3a63;
    --cyan: #1b9fd8;
    --paper: #f1f1f1;
    --ink: #0f2340;
    --text: #1f2a38;
    --rule: #d6d6d6;
  }
  * { margin: 0; padding: 0; box-sizing: border-box; }
  html, body { width: 942px; height: 1200px; overflow: hidden; }
  body {
    background: var(--backdrop);
    position: relative;
    font-family: "Montserrat", sans-serif;
  }
  .card {
    position: absolute;
    left: 160px;
    width: 623px;
    height: 345px;
    overflow: hidden;
    box-shadow: 0 18px 30px rgba(0,0,0,.45);
  }
  .card--front {
    top: 200px;
    background: linear-gradient(135deg, var(--navy-mid) 0%, var(--navy) 45%, var(--navy-deep) 100%);
  }
  .firm-mark {
    position: absolute;
    left: 0; right: 0;
    top: 150px;
    text-align: center;
    font-family: "DM Serif Display", serif;
    font-size: 28px;
    color: var(--cyan);
    letter-spacing: .5px;
  }
  .card--back { top: 610px; background: var(--paper); }
  .card__bands { position: absolute; inset: 0; }
  .holder-name {
    position: absolute;
    left: 0; right: 0;
    top: 154px;
    text-align: center;
    font-family: "DM Serif Display", serif;
    font-size: 27px;
    color: var(--ink);
  }
  .contact-row {
    position: absolute;
    left: 110px; right: 105px;
    top: 221px;
    height: 40px;
    border-top: 1px solid var(--rule);
    border-bottom: 1px solid var(--rule);
    display: flex;
    align-items: center;
    justify-content: center;
    gap: 12px;
    font-size: 12.5px;
    color: var(--text);
  }
  .contact-item { display: flex; align-items: center; gap: 4px; white-space: nowrap; }
  .contact-icon {
    width: 19px; height: 19px;
    background: var(--ink);
    display: flex; align-items: center; justify-content: center;
  }
  .address {
    position: absolute;
    left: 0; right: 0; top: 272px;
    text-align: center;
    font-size: 11px;
    color: var(--text);
  }
  .website {
    position: absolute;
    left: 0; right: 0; top: 317px;
    text-align: center;
    font-size: 10px;
    color: var(--text);
  }
</style>
</head>
<body>
  <section class="card card--front">
    <div class="firm-mark">Halloway &amp; Quintley, P.A.</div>
  </section>

  <section class="card card--back">
    <svg class="card__bands" width="623" height="345" viewBox="0 0 623 345" aria-hidden="true">
      <polygon points="0,0 623,0 623,147 311,74 0,147" fill="#122a4c"/>
      <polygon points="0,0 300,0 311,74 0,147" fill="#0f2444"/>
      <polygon points="300,0 623,0 623,40 311,74" fill="#17325a"/>
      <polygon points="311,74 623,20 623,147" fill="#0b1d38"/>
      <polygon points="400,0 623,0 623,60 520,50" fill="#1a3763" opacity=".6"/>
    </svg>
    <h1 class="holder-name">Derek T. Halloway, Esq.</h1>
    <div class="contact-row">
      <span class="contact-item">
        <span class="contact-icon">
          <svg width="12" height="12" viewBox="0 0 24 24" fill="none" stroke="#fff" stroke-width="1.8"><path d="M5 3h4l2 5-3 2a12 12 0 0 0 6 6l2-3 5 2v4a2 2 0 0 1-2 2A18 18 0 0 1 3 5a2 2 0 0 1 2-2z"/></svg>
        </span>(352) 555-0187
      </span>
      <span class="contact-item">
        <span class="contact-icon">
          <svg width="12" height="12" viewBox="0 0 24 24" fill="none" stroke="#fff" stroke-width="1.8"><rect x="6" y="3" width="12" height="6"/><rect x="3" y="9" width="18" height="8" rx="1"/><rect x="7" y="14" width="10" height="7"/></svg>
        </span>(352) 555-0142
      </span>
      <span class="contact-item">
        <span class="contact-icon">
          <svg width="12" height="12" viewBox="0 0 24 24" fill="none" stroke="#fff" stroke-width="1.8"><rect x="3" y="5" width="18" height="14"/><path d="M3 5l9 8 9-8"/></svg>
        </span>DerekH@hqlegalfx.com
      </span>
    </div>
    <p class="address">517 E. Quintley Blvd., P.O. Box 641, Tavares, FL 32790</p>
    <p class="website">www.HQLegalFX.com</p>
  </section>
</body>
</html>
```